TK Workshop - flyer

We are a machine shop. While making sales calls in the field, we need a flyer to leave behind with prospect to attract interest.

Target Market(s)

Medical device, aerospace and aviation component manfacturers

Font styles to use
Serif

Colors

Designer to choose colors to be used in the design.

Requirements
Must have
• NA
Nice to have
• NA
Should not have
• NA

```html
<!DOCTYPE html>
<html lang="en">
<head>
<meta charset="utf-8">
<title>TK Workshop – Titanium Spinal Screw Assemblies</title>
<link rel="stylesheet" href="https://fonts.googleapis.com/css2?family=Raleway:wght@300;400;500;600;700&family=Roboto:wght@400&family=PT+Sans:wght@700&display=swap">
<style>
:root{
  --red:#e4232b;
  --red-deep:#d3191f;
  --charcoal:#3b3c3f;
  --ink:#2a2a2a;
  --grey:#6f6f72;
  --paper:#ffffff;
  --mist:#f3f4f4;
  --photo-dark:#2a221e;
  --photo-warm:#4a3a30;
}
*{margin:0;padding:0;box-sizing:border-box}
html,body{width:846px;height:1200px;overflow:hidden;background:var(--paper)}
.flyer{position:relative;width:846px;height:1200px;overflow:hidden;font-family:"Raleway",sans-serif;color:var(--ink)}
.flyer__shapes{position:absolute;inset:0}
.abs{position:absolute}
.brand{left:46px;top:110px;display:flex;align-items:center;gap:12px}
.brand__name{font-family:"Raleway",sans-serif;font-weight:600;font-size:40px;color:var(--ink);letter-spacing:-.5px;line-height:1}
.brand__dot{width:30px;height:30px;border-radius:50%;background:var(--red)}
.headline{right:37px;top:78px;text-align:right;color:var(--paper);font-weight:400;font-size:54px;line-height:58px}
.headline__accent{display:block;color:var(--red);font-weight:700;font-size:56px}
.headline__rule{right:37px;top:257px;width:82px;height:3px;background:var(--red)}
.intro{right:35px;top:271px;width:300px;text-align:right;color:#e3ddd8;font-weight:300;font-size:16px;line-height:19.4px}
.section-title{left:59px;top:630px;font-size:31px;line-height:38px;font-weight:400;color:var(--ink)}
.section-title strong{display:block;color:var(--red);font-weight:700}
.section-title__rule{left:59px;top:708px;width:59px;height:3px;background:var(--charcoal)}
.lede{left:59px;top:724px;width:420px;font-size:23px;line-height:26px;font-weight:300;color:var(--grey)}
.capabilities{left:59px;top:795px;list-style:none}
.capabilities li{display:flex;align-items:center;height:41px;font-size:23px;font-weight:400;color:var(--charcoal)}
.capabilities li::before{content:"";width:16px;height:16px;border:2px solid var(--red);border-radius:50%;margin:0 38px 0 3px}
.markets{left:59px;top:1056px;font-size:24px;color:var(--red);font-weight:400}
.certified{left:59px;top:1088px;font-family:"PT Sans",sans-serif;font-weight:700;font-size:28px;color:var(--ink)}
.feature{width:210px;text-align:center;font-size:15px;line-height:20px;color:var(--paper)}
.feature__em{font-weight:700;color:var(--red);font-size:16px}
.feature--measure{left:505px;top:703px;line-height:19.5px}
.feature--measure .feature__em{color:var(--charcoal)}
.feature--clean{left:394px;top:904px}
.feature--temp{left:614px;top:904px}
.contact{color:var(--paper);font-family:"Roboto",sans-serif;font-size:18px;line-height:23px}
.contact--address{left:108px;top:1144px}
.contact--web{left:533px;top:1143px}
.contact--phone{left:533px;top:1173px}
</style>
</head>
<body>
<div class="flyer">
  <svg class="flyer__shapes" width="846" height="1200" viewBox="0 0 846 1200" aria-hidden="false">
    <defs>
      <linearGradient id="shopGrad" x1="0" y1="0" x2="1" y2="1">
        <stop offset="0" stop-color="#1e1a18"/>
        <stop offset=".45" stop-color="var(--photo-warm)"/>
        <stop offset="1" stop-color="#231d1a"/>
      </linearGradient>
      <linearGradient id="partsGrad" x1="0" y1="0" x2="1" y2="1">
        <stop offset="0" stop-color="#ffffff"/>
        <stop offset=".5" stop-color="#eef2ef"/>
        <stop offset="1" stop-color="#f7f7f7"/>
      </linearGradient>
    </defs>
    <rect class="shop-photo" x="0" y="0" width="846" height="830" fill="url(#shopGrad)" role="img" aria-label="Dimly lit machine shop interior behind the headline"/>
    <polygon class="brand-panel" points="0,0 316,0 405,135 339,260 0,260" fill="var(--mist)"/>
    <polygon class="lower-panel" points="0,590 465,590 846,806 846,1200 0,1200" fill="var(--paper)"/>
    <polygon class="diagonal-band" points="465,594 476,588 846,798 846,818" fill="var(--red)"/>
    <polygon class="parts-frame" points="0,259 465,259 561,428 465,600 0,600" fill="var(--red)"/>
    <polygon class="parts-photo" points="0,269 454,269 546,428 454,590 0,590" fill="url(#partsGrad)" role="img" aria-label="Coloured titanium pedicle screws, tulip heads and rings"/>
    <polygon class="hex hex--measure" points="610,574 723,638 723,767 610,832 497,767 497,638" fill="var(--paper)"/>
    <polygon class="hex hex--measure" points="610,578 719,640 719,765 610,828 501,765 501,640" fill="var(--red)"/>
    <rect class="hex-icon" x="551" y="640" width="118" height="52" rx="6" fill="var(--red-deep)" role="img" aria-label="Caliper icon"/>
    <polygon class="hex hex--clean" points="499,777 605,836 605,961 499,1021 393,961 393,836" fill="var(--red)"/>
    <polygon class="hex hex--clean" points="499,781 602,838 602,959 499,1017 396,959 396,838" fill="var(--charcoal)"/>
    <rect class="hex-icon" x="467" y="820" width="64" height="70" rx="6" fill="#48494c" role="img" aria-label="Cleaning hand icon"/>
    <polygon class="hex hex--temp" points="719,777 824,836 824,961 719,1021 612,961 612,836" fill="var(--red)"/>
    <polygon class="hex hex--temp" points="719,781 821,838 821,959 719,1017 615,959 615,838" fill="var(--charcoal)"/>
    <rect class="hex-icon" x="686" y="816" width="66" height="74" rx="6" fill="#48494c" role="img" aria-label="Thermometer icon"/>
    <rect class="footer" x="0" y="1124" width="846" height="76" fill="var(--charcoal)"/>
    <rect class="footer-stripe" x="0" y="1124" width="690" height="8" fill="var(--red)"/>
    <g class="icon icon--pin" fill="none" stroke="var(--red)" stroke-width="2.4">
      <circle cx="72" cy="1165" r="11"/>
      <path d="M72 1158c-3.5 0-6 2.6-6 5.8 0 4 6 9 6 9s6-5 6-9c0-3.2-2.5-5.8-6-5.8z"/>
      <circle cx="72" cy="1164" r="1.8" fill="var(--red)"/>
    </g>
    <g class="icon icon--web" fill="none" stroke="var(--red)" stroke-width="2">
      <circle cx="505" cy="1153" r="10"/>
      <circle cx="505" cy="1153" r="5.5"/>
      <path d="M499.5 1153h11M505 1147.5v11"/>
    </g>
    <g class="icon icon--phone" fill="none" stroke="var(--red)" stroke-width="2">
      <circle cx="505" cy="1183" r="10"/>
      <path d="M500 1178c0 6 4 10 10 10l1.5-2.5-3-2-1.5 1.5c-2-1-3.5-2.5-4.5-4.5l1.5-1.5-2-3z" fill="var(--red)" stroke="none"/>
    </g>
  </svg>

  <div class="abs brand"><span class="brand__name">TK Workshop</span><span class="brand__dot"></span></div>

  <h1 class="abs headline">Titanium<br>Spinal Screw<span class="headline__accent">Assemblies</span></h1>
  <div class="abs headline__rule"></div>
  <p class="abs intro">Our Education, Training, and 25 years of Medical and Aerospace machining experience helps us determine the best possible methods of manufacture that will be most cost effective for your parts.</p>

  <h2 class="abs section-title">OUR<strong>CAPABILITIES</strong></h2>
  <div class="abs section-title__rule"></div>
  <p class="abs lede">We make the parts, process them, and assemble them.</p>
  <ul class="abs capabilities">
    <li>5 axis cnc milling</li>
    <li>Turning</li>
    <li>Cnc swiss-type</li>
    <li>Deburring</li>
    <li>Vision scope 300</li>
    <li>Laser marking</li>
  </ul>

  <p class="abs feature feature--measure">Coordinate <span class="feature__em">Measuring</span><br>machines, comparators,<br>sur-face plated<br>micrometers</p>
  <p class="abs feature feature--clean">Ultrasonic<br><span class="feature__em">Cleaning &amp; Reverse</span><br>osmosis water</p>
  <p class="abs feature feature--temp">Dedicated<br><span class="feature__em">Temperature Controlled</span><br>room</p>

  <p class="abs markets">Medical, Implants, Aerospace, Aviation &amp; Military applications</p>
  <p class="abs certified">ISO 13485, 9100, 9001 CERTIFIED</p>

  <p class="abs contact contact--address">4120 Linden Road, Unit B,<br>Maple Grove, CA 90000</p>
  <p class="abs contact contact--web">www.tkworkshopcnc.com</p>
  <p class="abs contact contact--phone">(555) 014-2290</p>
</div>
</body>
</html>
```